Halvey Construction- Truck Wrap

I would like to advertise my residential construction company on our work truck

Target Market(s)

homeowners

Industry/Entity Type

residential construction

Colors
0054AA
0677BA
7BADD7
CADEEF
E8F1F8
F0912C
F2A743
F7CA91
FBE8D2
FDF5EE

Requirements
Must have
• company logo and type of work we do

```html
<!DOCTYPE html>
<html lang="en">
<head>
<meta charset="utf-8">
<title>Halvey Construction – Truck Wrap</title>
<link rel="stylesheet" href="https://fonts.googleapis.com/css2?family=Anton&family=Oswald:wght@600&display=swap">
<style>
  :root {
    --blue-deep: #0054AA;
    --blue-mid: #0677BA;
    --blue-soft: #7BADD7;
    --blue-pale: #CADEEF;
    --blue-mist: #E8F1F8;
    --orange: #F0912C;
    --white: #ffffff;
    --page: #ffffff;
  }
  html, body {
    margin: 0;
    width: 1012px;
    height: 1200px;
    overflow: hidden;
    background: var(--page);
  }
  .canvas { position: relative; width: 1012px; height: 1200px; }
  .wrap-panel { position: absolute; display: block; }
  .wrap-panel--driver { left: 120px; top: 140px; width: 715px; height: 240px; }
  .wrap-panel--passenger { left: 130px; top: 450px; width: 715px; height: 240px; }
  .wrap-panel--front { left: 298px; top: 815px; width: 310px; height: 250px; }
  .headline { font-family: "Anton", sans-serif; fill: var(--blue-deep); font-size: 24px; }
  .tagline { font-family: "Oswald", sans-serif; font-weight: 600; fill: var(--blue-deep); font-size: 8px; letter-spacing: 3px; }
  .brand-name { font-family: "Anton", sans-serif; fill: var(--blue-deep); font-size: 10px; letter-spacing: 0.5px; }
  .brand-square { fill: var(--blue-deep); }
</style>
</head>
<body>
<main class="canvas">

  <svg class="wrap-panel wrap-panel--driver" viewBox="0 0 715 240" aria-label="Driver side wrap">
    <defs>
      <linearGradient id="sheen" x1="0" y1="0" x2="1" y2="0">
        <stop offset="0" stop-color="#ffffff"/>
        <stop offset="0.5" stop-color="#E8F1F8"/>
        <stop offset="0.8" stop-color="#CADEEF"/>
        <stop offset="1" stop-color="#7BADD7"/>
      </linearGradient>
      <linearGradient id="glass" x1="0" y1="0" x2="1" y2="1">
        <stop offset="0" stop-color="#E8F1F8"/>
        <stop offset="0.5" stop-color="#7BADD7"/>
        <stop offset="1" stop-color="#CADEEF"/>
      </linearGradient>
    </defs>
    <rect class="wrap-base" width="715" height="240" fill="var(--white)"/>
    <polygon class="wrap-sheen" points="240,30 715,50 715,200 240,215" fill="url(#sheen)"/>
    <polygon class="wrap-photo" role="img" aria-label="Photo of glass high-rise buildings under construction with a tower crane" points="0,50 300,30 300,160 0,180" fill="url(#glass)"/>
    <polygon class="wrap-swoosh" points="470,45 715,60 715,235 600,150" fill="var(--blue-deep)"/>
    <g transform="rotate(-8 262 195)">
      <rect class="wrap-band" x="200" y="166" width="560" height="56" fill="var(--white)"/>
      <text class="headline" x="262" y="195">TRANSFORMING HOMES TO</text>
      <text class="tagline" x="318" y="211">REFLECT YOUR LIFESTYLE</text>
      <rect class="brand-square" x="510" y="172" width="7" height="7"/>
      <text class="brand-name" x="521" y="180">HALVEY</text>
      <text class="brand-name" x="510" y="192">CONSTRUCTION</text>
    </g>
  </svg>

  <svg class="wrap-panel wrap-panel--passenger" viewBox="0 0 715 240" aria-label="Passenger side wrap">
    <g transform="translate(715 0) scale(-1 1)">
      <rect class="wrap-base" width="715" height="240" fill="var(--white)"/>
      <polygon class="wrap-sheen" points="240,30 715,50 715,200 240,215" fill="url(#sheen)"/>
      <polygon class="wrap-photo" role="img" aria-label="Photo of glass high-rise buildings under construction with a tower crane" points="0,50 300,30 300,160 0,180" fill="url(#glass)"/>
      <polygon class="wrap-swoosh" points="470,45 715,60 715,235 600,150" fill="var(--blue-deep)"/>
    </g>
    <g transform="rotate(8 150 130)">
      <rect class="wrap-band" x="100" y="108" width="520" height="62" fill="var(--white)"/>
      <rect class="brand-square" x="150" y="124" width="7" height="7"/>
      <text class="brand-name" x="161" y="132">HALVEY</text>
      <text class="brand-name" x="150" y="144">CONSTRUCTION</text>
      <text class="headline" x="218" y="146">TRANSFORMING HOMES TO</text>
      <text class="tagline" x="218" y="161">REFLECT YOUR LIFESTYLE</text>
    </g>
  </svg>

  <svg class="wrap-panel wrap-panel--front" viewBox="0 0 310 250" aria-label="Front wrap">
    <defs>
      <linearGradient id="front-fade" x1="0" y1="0" x2="1" y2="0">
        <stop offset="0" stop-color="#0054AA"/>
        <stop offset="0.3" stop-color="#0677BA"/>
        <stop offset="0.55" stop-color="#7BADD7"/>
        <stop offset="0.8" stop-color="#E8F1F8"/>
        <stop offset="1" stop-color="#ffffff"/>
      </linearGradient>
    </defs>
    <rect class="wrap-base" width="310" height="250" fill="var(--white)"/>
    <path class="wrap-roof" d="M45,0 H265 L255,24 H55 Z" fill="var(--blue-deep)"/>
    <path class="wrap-sheen" d="M0,60 Q150,55 310,80 V250 H0 Z" fill="url(#front-fade)"/>
    <path class="wrap-swoosh" d="M40,60 Q200,58 310,75 V105 Q220,78 120,68 Z" fill="var(--blue-deep)"/>
    <rect class="wrap-clear" x="0" y="200" width="310" height="50" fill="var(--white)" opacity="0.6"/>
  </svg>

</main>
</body>
</html>
```